stars + comments Reviews website design (similar to grubly concept)

Please refer to attached logo and wire frames
----------------------------------------------------------------------------------------------------
we are a company based in egypt, seeking a design for a website that allows user to find doctors using search and filters.
also it allows user to review this doctor through providing comment and 1 to 5 stars
i need 4 main pages designs:
1- Doctors list/favorites list
2- Doctor view
3- Add doctor (3 steps)
4- Sign-in/sign up
5- Menu design
am into the colors teal/turquoise (though am open for different opinion)
i don't want the design theme to be doctors specific
am into the school of very clean, very neat, very simple
(chirpnet, pagecircle, snapmosaic designs are appealing to me)
Updates

Number of Pages Required

4 page

Font styles to use
Sans Serif

Colors
00a990
33b8a4

Requirements
Must have
• website will be bilingual/ bi-directional (English and Arabic)
• designer needs to provide another copy of the design with "right to left" orientation
• interactive button animation

```html
<!DOCTYPE html>
<html lang="en">
<head>
<meta charset="utf-8">
<title>Curalist – Add Doctor</title>
<link href="https://fonts.googleapis.com/css2?family=Open+Sans:wght@400;600;700&family=Arimo:wght@700&display=swap" rel="stylesheet">
<style>
:root{
  --teal-top:#0cc3c1;
  --teal-bottom:#049e9c;
  --teal-text:#0f9e99;
  --star:#0d9f9a;
  --star-off:#d4d4d4;
  --page:#f0f0f0;
  --card:#ffffff;
  --card-border:#e2e2e2;
  --ink:#333333;
  --ink-soft:#555555;
  --footer-top:#474747;
  --footer-bottom:#333333;
  --white:#ffffff;
}
*{box-sizing:border-box;margin:0;padding:0}
html,body{width:1200px;height:922px;overflow:hidden}
body{position:relative;background:var(--page);font-family:"Open Sans",Arial,sans-serif;color:var(--ink)}
.site-header{position:absolute;left:0;top:0;width:1200px;height:107px;background:linear-gradient(var(--teal-top),var(--teal-bottom));box-shadow:0 2px 3px rgba(0,0,0,.12)}
.brand{position:absolute;left:133px;top:40px;display:flex;align-items:center;gap:8px;color:var(--white);font-size:28px;font-weight:600}
.brand-mark{width:26px;height:26px;border-radius:50%;background:var(--white)}
.main-nav{position:absolute;left:410px;top:21px;display:flex}
.nav-item{width:70px;text-align:center;color:var(--white);font-size:13px;font-weight:600}
.nav-icon{width:44px;height:44px;margin:0 auto 10px;border-radius:50%;background:rgba(0,0,0,.08);display:flex;align-items:center;justify-content:center}
.user{position:absolute;left:783px;top:39px;display:flex;align-items:center;gap:12px;color:var(--white);font-size:14px;font-weight:600}
.user-avatar{width:48px;height:48px;border-radius:50%;border:3px solid var(--white);background:linear-gradient(135deg,#c9a48c,#7a5a4a)}
.caret{display:inline-block;width:0;height:0;border-left:4px solid transparent;border-right:4px solid transparent;border-top:5px solid currentColor;margin-left:6px;vertical-align:middle}
.language{position:absolute;left:956px;top:49px;width:113px;height:34px;border:2px solid rgba(255,255,255,.6);display:flex;align-items:center;padding-left:9px;gap:7px;color:var(--white);font-size:13px;font-weight:600}
.language .caret{margin-left:18px}
.breadcrumb{position:absolute;left:137px;top:143px;font-size:14px;color:var(--ink)}
.filters{position:absolute;left:133px;top:201px;width:204px}
.filter{height:36px;margin-bottom:16px;border-radius:18px;background:var(--white);border:1px solid #dedede;box-shadow:inset 0 2px 2px rgba(0,0,0,.06);display:flex;align-items:center;justify-content:space-between;padding:0 16px 0 19px;font-size:13px;color:var(--ink-soft)}
.filter .caret{color:#777}
.filter-button{margin-top:6px;height:36px;border-radius:18px;background:linear-gradient(var(--teal-top),var(--teal-bottom));color:var(--white);font-size:12px;font-weight:600;letter-spacing:.6px;display:flex;align-items:center;justify-content:center}
.results-count{position:absolute;left:409px;top:199px;font-family:Arimo,Arial,sans-serif;font-weight:700;font-size:16px;color:var(--ink)}
.doctor-card{position:absolute;left:409px;width:660px;height:130px;background:var(--card);border:1px solid var(--card-border)}
.doctor-photo{position:absolute;left:22px;top:24px;width:79px;height:79px}
.doctor-info{position:absolute;left:118px;top:25px;font-size:13px;line-height:21px;color:var(--ink-soft)}
.doctor-name{font-size:15px;color:var(--teal-text);margin-bottom:6px}
.doctor-name small{font-size:12px;color:var(--ink-soft)}
.doctor-info p{padding-left:3px}
.rating{position:absolute;right:31px;top:37px;display:flex;align-items:center;gap:6px;font-size:13px;color:var(--ink-soft)}
.stars{display:flex;gap:1px}
.favorite{position:absolute;right:29px;top:69px;width:40px;height:40px;border-radius:50%;background:#ececec;display:flex;align-items:center;justify-content:center}
.site-footer{position:absolute;left:0;top:837px;width:1200px;height:85px;background:linear-gradient(var(--footer-top),var(--footer-bottom))}
.copyright{position:absolute;left:132px;top:41px;font-size:13px;color:var(--white)}
.social{position:absolute;left:895px;top:32px;display:flex;gap:5px}
.social-link{width:31px;height:31px;border-radius:50%;background:var(--white);color:var(--footer-bottom);font-size:12px;font-weight:700;display:flex;align-items:center;justify-content:center}
</style>
</head>
<body>
<header class="site-header">
  <div class="brand"><span class="brand-mark"></span>Curalist</div>
  <nav class="main-nav">
    <div class="nav-item"><div class="nav-icon"><svg width="20" height="18" viewBox="0 0 20 18"><path d="M10 1 1 9h3v8h4v-5h4v5h4V9h3z" fill="#fff"/></svg></div>Home</div>
    <div class="nav-item"><div class="nav-icon"><svg width="24" height="21" viewBox="0 0 24 21"><path d="M12 20 2.5 11C-1 7.5 1.5 1 6.5 1 9 1 11 2.5 12 4.5 13 2.5 15 1 17.5 1c5 0 7.5 6.5 4 10z" fill="#fff"/></svg></div>Care</div>
    <div class="nav-item"><div class="nav-icon"><svg width="20" height="20" viewBox="0 0 20 20"><circle cx="10" cy="5" r="4" fill="#fff"/><path d="M2 19c0-5 3.5-8 8-8s8 3 8 8z" fill="#fff"/><circle cx="10" cy="15" r="2" fill="none" stroke="#07aaa8" stroke-width="1.5"/></svg></div>Doctor</div>
    <div class="nav-item"><div class="nav-icon"><svg width="18" height="18" viewBox="0 0 18 18"><circle cx="7.5" cy="7.5" r="5" fill="none" stroke="#fff" stroke-width="2.5"/><path d="m11 11 5 5" stroke="#fff" stroke-width="3" stroke-linecap="round"/></svg></div>Search</div>
  </nav>
  <div class="user"><div class="user-avatar" role="img" aria-label="User profile photo"></div><span>Omar Sami<span class="caret"></span></span></div>
  <div class="language">
    <svg width="17" height="11" viewBox="0 0 17 11"><rect width="17" height="11" fill="#23326e"/><path d="M0 0 17 11M17 0 0 11" stroke="#fff" stroke-width="2"/><path d="M8.5 0v11M0 5.5h17" stroke="#fff" stroke-width="3"/><path d="M8.5 0v11M0 5.5h17" stroke="#c8102e" stroke-width="1.6"/></svg>
    English<span class="caret"></span>
  </div>
</header>

<div class="breadcrumb">Home - Favorites - Add Doctor</div>

<aside class="filters">
  <div class="filter">Specialization<span class="caret"></span></div>
  <div class="filter">Sub-Specialization<span class="caret"></span></div>
  <div class="filter">Area<span class="caret"></span></div>
  <div class="filter">Gender<span class="caret"></span></div>
  <div class="filter">Rating<span class="caret"></span></div>
  <div class="filter-button">FILTER HERE</div>
</aside>

<h1 class="results-count">15,123&nbsp; Doctors</h1>

<svg width="0" height="0" style="position:absolute">
  <defs>
    <path id="star" d="M6.5 0.5 8.3 4.4 12.5 4.8 9.3 7.6 10.3 11.8 6.5 9.6 2.7 11.8 3.7 7.6 0.5 4.8 4.7 4.4z"/>
    <path id="heart" d="M8 14 2 8.3C-.5 5.8 1 1.5 4.5 1.5 6 1.5 7.3 2.5 8 3.8 8.7 2.5 10 1.5 11.5 1.5 15 1.5 16.5 5.8 14 8.3z"/>
  </defs>
</svg>

<article class="doctor-card" style="top:238px">
  <div class="doctor-photo" role="img" aria-label="Portrait photo of the doctor" style="background:linear-gradient(135deg,#e8e4df,#b89a86 60%,#6b6f78)"></div>
  <div class="doctor-info"><div class="doctor-name">Karim Adel <small>(1Km away)</small></div><p>Anesthesiologist</p><p>18 Nour Street, Dokki</p></div>
  <div class="rating">Rating: <span class="stars"><svg width="13" height="13"><use href="#star" fill="var(--star)"/></svg><svg width="13" height="13"><use href="#star" fill="var(--star)"/></svg><svg width="13" height="13"><use href="#star" fill="var(--star)"/></svg><svg width="13" height="13"><use href="#star" fill="var(--star)"/></svg><svg width="13" height="13"><use href="#star" fill="var(--star-off)"/></svg></span>&nbsp;(123)</div>
  <div class="favorite"><svg width="16" height="16"><use href="#heart" fill="none" stroke="#444" stroke-width="1.4"/></svg></div>
</article>

<article class="doctor-card" style="top:380px">
  <div class="doctor-photo" role="img" aria-label="Portrait photo of the doctor" style="background:linear-gradient(135deg,#7fa36a,#e3cfa0 50%,#f2eee8)"></div>
  <div class="doctor-info"><div class="doctor-name">Nora Fahmy <small>(1Km away)</small></div><p>Anesthesiologist</p><p>18 Nour Street, Dokki</p></div>
  <div class="rating">Rating: <span class="stars"><svg width="13" height="13"><use href="#star" fill="var(--star)"/></svg><svg width="13" height="13"><use href="#star" fill="var(--star)"/></svg><svg width="13" height="13"><use href="#star" fill="var(--star)"/></svg><svg width="13" height="13"><use href="#star" fill="var(--star)"/></svg><svg width="13" height="13"><use href="#star" fill="var(--star-off)"/></svg></span>&nbsp;(123)</div>
  <div class="favorite"><svg width="16" height="16"><use href="#heart" fill="none" stroke="#444" stroke-width="1.4"/></svg></div>
</article>

<article class="doctor-card" style="top:521px">
  <div class="doctor-photo" role="img" aria-label="Portrait photo of the doctor" style="background:linear-gradient(135deg,#dfe3e8,#c49c84 55%,#4c5f7a)"></div>
  <div class="doctor-info"><div class="doctor-name">Hany Lotfy <small>(1Km away)</small></div><p>Anesthesiologist</p><p>18 Nour Street, Dokki</p></div>
  <div class="rating">Rating: <span class="stars"><svg width="13" height="13"><use href="#star" fill="var(--star)"/></svg><svg width="13" height="13"><use href="#star" fill="var(--star)"/></svg><svg width="13" height="13"><use href="#star" fill="var(--star)"/></svg><svg width="13" height="13"><use href="#star" fill="var(--star)"/></svg><svg width="13" height="13"><use href="#star" fill="var(--star-off)"/></svg></span>&nbsp;(123)</div>
  <div class="favorite"><svg width="16" height="16"><use href="#heart" fill="none" stroke="#444" stroke-width="1.4"/></svg></div>
</article>

<article class="doctor-card" style="top:662px">
  <div class="doctor-photo" role="img" aria-label="Portrait photo of the doctor" style="background:linear-gradient(135deg,#f0ece6,#b8907a 50%,#7aa6cf)"></div>
  <div class="doctor-info"><div class="doctor-name">Tarek Nabil <small>(1Km away)</small></div><p>Anesthesiologist</p><p>18 Nour Street, Dokki</p></div>
  <div class="rating">Rating: <span class="stars"><svg width="13" height="13"><use href="#star" fill="var(--star)"/></svg><svg width="13" height="13"><use href="#star" fill="var(--star)"/></svg><svg width="13" height="13"><use href="#star" fill="var(--star)"/></svg><svg width="13" height="13"><use href="#star" fill="var(--star)"/></svg><svg width="13" height="13"><use href="#star" fill="var(--star-off)"/></svg></span>&nbsp;(123)</div>
  <div class="favorite"><svg width="16" height="16"><use href="#heart" fill="none" stroke="#444" stroke-width="1.4"/></svg></div>
</article>

<footer class="site-footer">
  <p class="copyright">Copyright (c) 2105 Yoursite All Right Reserved</p>
  <nav class="social">
    <span class="social-link" aria-label="pagecircle">p</span>
    <span class="social-link" aria-label="photoblot">b</span>
    <span class="social-link" aria-label="chirpnet">c</span>
    <span class="social-link" aria-label="plusring">r</span>
    <span class="social-link" aria-label="Feed"><svg width="13" height="13" viewBox="0 0 13 13"><circle cx="2" cy="11" r="1.8" fill="#333"/><path d="M1 6a6 6 0 0 1 6 6M1 1.5A10.5 10.5 0 0 1 11.5 12" fill="none" stroke="#333" stroke-width="2"/></svg></span>
  </nav>
</footer>
</body>
</html>
```